PKD Business Card

Looking for a business card for my restaurant group I own. Four different concepts:

Bramblecrest Alehall
Vellory Alehall
Tamrack's Stone Hearth Kitchen
Cobblestead Patty Works

Card doesn't need to include all the logos.

```html
<!DOCTYPE html>
<html lang="en">
<head>
<meta charset="utf-8">
<title>PKD Business Card</title>
<link href="https://fonts.googleapis.com/css2?family=Montserrat:wght@500;600;700&family=Lato:wght@400;700&display=swap" rel="stylesheet">
<style>
  :root {
    --stage: #3b3c3f;
    --card-grey: #6d6e71;
    --card-white: #ffffff;
    --gold: #c9a55c;
    --ink-grey: #58595b;
    --line-grey: #9a9b9e;
    --soft-white: #f4f4f4;
  }
  * { margin: 0; padding: 0; box-sizing: border-box; }
  html, body { width: 1200px; height: 900px; overflow: hidden; }
  body {
    background: var(--stage);
    position: relative;
    font-family: "Lato", sans-serif;
  }
  .card {
    position: absolute;
    width: 540px;
    height: 310px;
    border-radius: 26px;
    overflow: hidden;
    box-shadow: 0 14px 30px rgba(0,0,0,0.35);
  }

  /* Back side */
  .card-back {
    left: 80px; top: 110px;
    background: var(--card-grey);
    border-bottom: 7px solid var(--gold);
    display: flex; flex-direction: column; align-items: center;
    padding-top: 58px;
  }
  .brand {
    font-family: "Montserrat", sans-serif;
    font-weight: 600;
    text-align: center;
    display: flex; flex-direction: column; align-items: center;
  }
  .brand-initials { font-size: 46px; letter-spacing: 4px; line-height: 1; }
  .brand-name { font-size: 17px; letter-spacing: 3px; margin-top: 10px; text-transform: uppercase; }
  .card-back .brand { color: var(--soft-white); }
  .divider-h {
    width: 340px; height: 1px; background: var(--line-grey);
    margin: 24px 0 18px;
  }
  .concepts {
    list-style: none;
    display: flex; flex-wrap: wrap; justify-content: center;
    gap: 8px 22px;
    width: 460px;
    color: var(--soft-white);
    font-size: 13.5px;
  }
  .concepts li { display: flex; align-items: center; }
  .concepts li::before {
    content: ""; width: 6px; height: 6px; border-radius: 50%;
    background: var(--gold); margin-right: 8px;
  }

  /* Front side */
  .card-front {
    left: 580px; top: 480px;
    background: var(--card-white);
    border-bottom: 7px solid #cfcfcf;
    display: flex; align-items: center;
  }
  .card-front .brand {
    color: var(--gold);
    width: 250px;
  }
  .card-front .brand-name { font-size: 15px; }
  .divider-v {
    width: 1px; height: 170px; background: var(--line-grey);
  }
  .contact { padding-left: 28px; }
  .person-name {
    font-family: "Montserrat", sans-serif;
    font-weight: 700; font-size: 22px;
    color: var(--gold); text-transform: uppercase; letter-spacing: 0.5px;
  }
  .person-role { color: var(--ink-grey); font-size: 15px; margin: 2px 0 16px; }
  .contact-list { list-style: none; }
  .contact-list li {
    display: flex; align-items: center; gap: 10px;
    color: var(--ink-grey); font-size: 13.5px; margin-bottom: 8px;
  }
  .contact-list svg { width: 14px; height: 14px; flex: none; }
</style>
</head>
<body>

  <section class="card card-back" aria-label="Card back">
    <div class="brand">
      <span class="brand-initials">PKD</span>
      <span class="brand-name">Parkdale Kinship Dining</span>
    </div>
    <div class="divider-h"></div>
    <ul class="concepts">
      <li>Bramblecrest Alehall</li>
      <li>Vellory Alehall</li>
      <li>Tamrack's Stone Hearth Kitchen</li>
      <li>Cobblestead Patty Works</li>
    </ul>
  </section>

  <section class="card card-front" aria-label="Card front">
    <div class="brand">
      <span class="brand-initials">PKD</span>
      <span class="brand-name">Parkdale Kinship Dining</span>
    </div>
    <div class="divider-v"></div>
    <div class="contact">
      <h1 class="person-name">Marisa Delcourt</h1>
      <p class="person-role">Owner</p>
      <ul class="contact-list">
        <li>
          <svg viewBox="0 0 24 24" aria-hidden="true"><path fill="#c9a55c" d="M6.6 10.8a15.1 15.1 0 0 0 6.6 6.6l2.2-2.2a1 1 0 0 1 1-.25 11.4 11.4 0 0 0 3.6.57 1 1 0 0 1 1 1V20a1 1 0 0 1-1 1A17 17 0 0 1 3 4a1 1 0 0 1 1-1h3.5a1 1 0 0 1 1 1c0 1.25.2 2.45.57 3.57a1 1 0 0 1-.25 1z"/></svg>
          555.204.7391
        </li>
        <li>
          <svg viewBox="0 0 24 24" aria-hidden="true"><rect x="2" y="5" width="20" height="14" rx="1.5" fill="#c9a55c"/><path d="M3 6l9 7 9-7" fill="none" stroke="#fff" stroke-width="1.6"/></svg>
          marisadelcourt@inboxmail.com
        </li>
        <li>
          <svg viewBox="0 0 24 24" aria-hidden="true"><g fill="none" stroke="#c9a55c" stroke-width="1.8"><circle cx="12" cy="12" r="9.5"/><ellipse cx="12" cy="12" rx="4" ry="9.5"/><path d="M2.5 12h19M4 7h16M4 17h16"/></g></svg>
          www.parkdalekinshipdining.com
        </li>
      </ul>
    </div>
  </section>

</body>
</html>
```